Business Card Design needed for logo design project

This project is linked to Veltrix Ember Social Media Logo.

Our company needs a Business Card Design. Please refer to our original project in the link above.

Industry/Entity Type

Business

```html
<!DOCTYPE html>
<html lang="en">
<head>
<meta charset="utf-8">
<title>Veltrix Ember — Business Card</title>
<link rel="stylesheet" href="https://fonts.googleapis.com/css2?family=Arimo:wght@400;700&display=swap">
<style>
  :root {
    --canvas: #e9eaec;
    --card-dark: #2b2b2b;
    --card-light: #fbfbfb;
    --ink: #2b2b2b;
    --white: #ffffff;
    --accent: #4a8fd8;
    --shadow: rgba(0, 0, 0, 0.22);
  }
  * { box-sizing: border-box; margin: 0; padding: 0; }
  html, body {
    width: 1085px;
    height: 1200px;
    overflow: hidden;
    background: var(--canvas);
    font-family: "Arimo", Arial, sans-serif;
  }
  .canvas {
    position: relative;
    width: 1085px;
    height: 1200px;
  }
  .card {
    position: absolute;
    left: 112px;
    width: 860px;
    height: 492px;
    border-radius: 4px;
    box-shadow: 0 18px 40px var(--shadow);
    overflow: hidden;
  }
  .card--front { top: 64px; background: var(--card-dark); color: var(--white); }
  .card--back  { top: 644px; background: var(--card-light); color: var(--ink); }

  .brand {
    display: flex;
    align-items: center;
    gap: 12px;
    white-space: nowrap;
  }
  .brand__mark {
    flex: none;
    width: 26px;
    height: 26px;
    background: var(--accent);
  }
  .brand__text { display: flex; flex-direction: column; }
  .brand__name {
    font-weight: 400;
    text-transform: uppercase;
    letter-spacing: 1px;
    line-height: 1;
  }
  .brand__tagline {
    font-weight: 700;
    margin-top: 6px;
  }

  .card--front .brand {
    position: absolute;
    top: 44px;
    left: 44px;
  }
  .card--front .brand__name { font-size: 26px; color: var(--white); }
  .card--front .brand__tagline { font-size: 10px; color: var(--white); }

  .contact {
    position: absolute;
    left: 70px;
    top: 222px;
  }
  .contact__name {
    font-size: 38px;
    color: var(--accent);
    margin-bottom: 30px;
  }
  .contact__line {
    font-size: 25px;
    line-height: 36px;
    color: var(--white);
  }

  .card--back .brand {
    position: absolute;
    top: 50%;
    left: 50%;
    transform: translate(-50%, -50%);
    gap: 18px;
  }
  .card--back .brand__mark { width: 46px; height: 46px; }
  .card--back .brand__name { font-size: 46px; color: var(--ink); }
  .card--back .brand__tagline { font-size: 15px; color: var(--ink); margin-top: 10px; }
</style>
</head>
<body>
<main class="canvas">
  <section class="card card--front" aria-label="Business card front">
    <div class="brand">
      <span class="brand__mark"></span>
      <div class="brand__text">
        <span class="brand__name">Veltrix Ember</span>
        <span class="brand__tagline">Property Guidance Close to Home</span>
      </div>
    </div>
    <div class="contact">
      <p class="contact__name">Idris Malouf</p>
      <p class="contact__line">555-210-348</p>
      <p class="contact__line">idris@veltrixember.com</p>
      <p class="contact__line">veltrixember.com</p>
    </div>
  </section>

  <section class="card card--back" aria-label="Business card back">
    <div class="brand">
      <span class="brand__mark"></span>
      <div class="brand__text">
        <span class="brand__name">Veltrix Ember</span>
        <span class="brand__tagline">Property Guidance Close to Home</span>
      </div>
    </div>
  </section>
</main>
</body>
</html>
```